Design a van wrap

We require a full van wrap design for a construction and development company. The design must present a premium, professional, and highly visible brand image suitable for a modern construction business. See attached existing wrap. Require a whole new look.
Vehicle Details
- Vehicle: Velbro electric van (T7 / similar size)
- Wrap type: Full wrap (bonnet, sides, rear)
- Use Palmet image on the rear doors
Dimension uCarrio 8 L1H1 uCarrio 8 L2H1
Overall length ~4,800 mm ~5,250 mm
Overall width (excl. mirrors) ~1,874 mm ~1,874 mm
Overall height (H1) ~1,960 mm ~1,960 mm
Wheelbase ~3,100 mm ~3,450 mm
Roof height H1 (standard) H1 (standard)
Branding
- Company Name: KORVELT
- Industry: Construction & Development
- 4 bullets on each side of van detailing scope of business
- New Builds
- Basement Works
- Piling Works
- Demolition
- Engineering
- RC Frame Works
- Loft Conversions
- Refurbishment
Brand Style: Modern, strong, premium, clean
- Colours:
- Primary: Black and Brown
- Accent: Cream (for contrast and legibility if required - see business card)
- Existing assets: Logo will be provided (vector format)
Design Style & Finish
- Contemporary and bold
- Strong contrast for roadside visibility
- Suitable for commercial vinyl printing
- Avoid over-complication or excessive textures
Deliverables
- Print-ready files
- Vector format preferred (AI / EPS / PDF)
- High-resolution mockups showing all sides of the van
- Colour codes specified (CMYK / Pantone if applicable)
Target Outcome
A van wrap that clearly communicates professionalism, scale, and trust, stands out on the road, and reinforces a premium construction brand.

```html
<!DOCTYPE html>
<html lang="en">
<head>
<meta charset="utf-8">
<title>KORVELT Van Wrap – Side Elevation</title>
<link rel="stylesheet" href="https://fonts.googleapis.com/css2?family=Montserrat:wght@700&family=Oswald:wght@600;700&family=Roboto+Condensed:wght@400;500&display=swap">
<style>
  :root {
    --canvas: #ffffff;
    --body-light: #b3a590;
    --body-mid: #a39480;
    --body-dark: #8d7f6c;
    --accent-warm: #b98a55;
    --ink: #141414;
    --glass: #3d4441;
    --trim: #2a2a2a;
    --tyre: #1c1c1c;
    --hub: #e6e6e6;
  }
  html, body {
    margin: 0;
    padding: 0;
    width: 1200px;
    height: 1200px;
    overflow: hidden;
    background: var(--canvas);
  }
  .van-wrap { display: block; width: 1200px; height: 1200px; }
  .body-panel { fill: url(#bodyShade); }
  .wrap-graphic-area { fill: url(#warmTone); }
  .panel-seam { stroke: #6f6455; stroke-width: 2; fill: none; opacity: .6; }
  .glass { fill: var(--glass); }
  .trim { fill: var(--trim); }
  .tyre { fill: var(--tyre); }
  .hub { fill: var(--hub); }
  .hub-center { fill: #9c9c9c; }
  .ground-shadow { fill: #000; opacity: .18; }
  .brand-mark { fill: none; stroke: var(--ink); stroke-width: 4; }
  .brand-name {
    font-family: "Montserrat", sans-serif;
    font-weight: 700;
    font-size: 25px;
    letter-spacing: 5px;
    fill: var(--ink);
  }
  .headline {
    font-family: "Oswald", sans-serif;
    font-weight: 700;
    fill: var(--ink);
  }
  .headline--top { font-size: 29px; }
  .headline--main { font-size: 36px; }
  .service-item {
    font-family: "Roboto Condensed", sans-serif;
    font-weight: 400;
    font-size: 21px;
    fill: var(--ink);
  }
  .phone {
    font-family: "Oswald", sans-serif;
    font-weight: 600;
    font-size: 27px;
    letter-spacing: 1.5px;
    fill: var(--ink);
  }
  .website {
    font-family: "Roboto Condensed", sans-serif;
    font-weight: 500;
    font-size: 21px;
    fill: var(--ink);
  }
</style>
</head>
<body>
<svg class="van-wrap" viewBox="0 0 1200 1200" xmlns="http://www.w3.org/2000/svg" aria-label="KORVELT van wrap, side view">
  <defs>
    <linearGradient id="bodyShade" x1="0" y1="0" x2="0" y2="1">
      <stop offset="0" stop-color="var(--body-dark)"/>
      <stop offset=".15" stop-color="var(--body-light)"/>
      <stop offset=".8" stop-color="var(--body-mid)"/>
      <stop offset="1" stop-color="var(--body-dark)"/>
    </linearGradient>
    <linearGradient id="warmTone" x1="0" y1="0" x2="1" y2="1">
      <stop offset="0" stop-color="var(--accent-warm)" stop-opacity="0"/>
      <stop offset=".6" stop-color="var(--accent-warm)" stop-opacity=".16"/>
      <stop offset="1" stop-color="var(--accent-warm)" stop-opacity="0"/>
    </linearGradient>
    <clipPath id="bodyClip">
      <path d="M130 420 L690 428 Q740 430 790 470 L1030 605 Q1090 625 1095 660 L1100 800 Q1100 822 1080 825 L120 818 Q100 815 100 795 L100 450 Q100 420 130 420 Z"/>
    </clipPath>
  </defs>

  <ellipse class="ground-shadow" cx="600" cy="868" rx="540" ry="12"/>

  <g class="van-body">
    <path class="body-panel" d="M130 420 L690 428 Q740 430 790 470 L1030 605 Q1090 625 1095 660 L1100 800 Q1100 822 1080 825 L120 818 Q100 815 100 795 L100 450 Q100 420 130 420 Z"/>

    <g class="wrap-graphics" clip-path="url(#bodyClip)">
      <rect class="wrap-graphic-area" role="img" aria-label="Flowing gold pinstripe wave graphic across the van body" x="100" y="420" width="1000" height="405"/>
    </g>

    <path class="panel-seam" d="M431 432 L431 818 M675 432 L675 818 M100 485 L690 490"/>
    <path class="panel-seam" d="M220 612 L431 612"/>

    <path class="glass" d="M715 505 L848 505 Q870 508 895 560 L905 605 L715 605 Z"/>
    <path class="glass" d="M880 515 L1015 600 L935 605 Z" opacity=".85"/>
    <path class="trim" d="M1025 635 Q1085 640 1095 665 L1070 668 Q1040 650 1025 648 Z"/>
    <rect class="trim" x="860" y="575" width="28" height="50" rx="8"/>
    <rect class="trim" x="648" y="648" width="78" height="22" rx="10"/>
    <rect class="trim" x="465" y="775" width="375" height="24" rx="12"/>
  </g>

  <g class="wheel wheel--rear">
    <path d="M230 820 A80 80 0 0 1 390 820 Z" fill="#fff"/>
    <circle class="tyre" cx="310" cy="810" r="68"/>
    <circle class="hub" cx="310" cy="810" r="44"/>
    <circle class="hub-center" cx="310" cy="810" r="12"/>
  </g>
  <g class="wheel wheel--front">
    <path d="M895 820 A80 80 0 0 1 1055 820 Z" fill="#fff"/>
    <circle class="tyre" cx="975" cy="810" r="68"/>
    <circle class="hub" cx="975" cy="810" r="44"/>
    <circle class="hub-center" cx="975" cy="810" r="12"/>
  </g>

  <g class="brand">
    <rect class="brand-mark" x="289" y="508" width="40" height="40"/>
    <text class="brand-name" x="310" y="575" text-anchor="middle">KORVELT</text>
  </g>

  <g class="headline-block">
    <text class="headline headline--top" x="448" y="542">CONSTRUCTION &amp;</text>
    <text class="headline headline--main" x="448" y="580">DEVELOPMENT</text>
  </g>

  <g class="services">
    <text class="service-item" x="450" y="643">- New Builds</text>
    <text class="service-item" x="450" y="673">- Basement Works</text>
    <text class="service-item" x="450" y="704">- Piling Works</text>
    <text class="service-item" x="450" y="734">- Demolition</text>
  </g>

  <g class="contact">
    <text class="phone" x="702" y="706">08001 472 905</text>
    <text class="website" x="702" y="735">www.korvelt.co.uk</text>
  </g>
</svg>
</body>
</html>
```